Business Card Design

our business is purchasing, rehabbing and flipping homes. Design a house in the palm of a hand. This card is for a new company based in Georgia. So we buy homes that have been foreclosed, short sales,abandond, old homes and vacant homes.
We help improve the communities that we work in. We would like to see designs that use a black background with green accent and other colors that blend and don't take away from the logo and other important information.

Industry/Entity Type

Business

Contact Information for Business Card

Mavenbrook Holdings
Turning Old Doors Into New Starts
2738 Fenwick Lane
Duluth GA 30418
Office: 678-555-0192
mavenbrookholdingsllc.example

```html
<!DOCTYPE html>
<html lang="en">
<head>
<meta charset="utf-8">
<title>Mavenbrook Holdings — Business Card</title>
<link rel="stylesheet" href="https://fonts.googleapis.com/css2?family=Anton&family=Oswald:wght@500&family=Roboto:wght@300&display=swap">
<style>
  :root {
    --card-dark: #333333;
    --green-deep: #4f9a0c;
    --green-main: #6bb82a;
    --green-light: #a6dc4e;
    --text-white: #ffffff;
    --outline-dark: #2a2a2a;
    --page-bg: #e9e9e9;
  }
  html, body {
    margin: 0;
    padding: 0;
    width: 1200px;
    height: 778px;
    overflow: hidden;
    background: var(--page-bg);
  }
  .card {
    position: relative;
    width: 1200px;
    height: 778px;
    background: var(--card-dark);
    overflow: hidden;
  }
  .card-shape {
    position: absolute;
    inset: 0;
  }
  .company-title {
    position: absolute;
    top: 26px;
    left: 0;
    width: 100%;
    margin: 0;
    text-align: center;
    font-family: "Anton", sans-serif;
    font-weight: 400;
    font-size: 86px;
    letter-spacing: 2px;
    color: var(--text-white);
    -webkit-text-stroke: 2px var(--outline-dark);
    text-shadow: 4px 4px 0 var(--outline-dark);
    line-height: 1.2;
  }
  .brand-mark {
    position: absolute;
    left: 92px;
    top: 300px;
    width: 380px;
    display: flex;
    flex-direction: column;
    align-items: center;
    gap: 18px;
  }
  .brand-dot {
    width: 90px;
    height: 90px;
    border-radius: 50%;
    background: var(--green-main);
  }
  .brand-name {
    font-family: "Oswald", sans-serif;
    font-weight: 500;
    font-size: 46px;
    line-height: 1.1;
    color: var(--green-light);
    text-align: center;
    margin: 0;
  }
  .tagline {
    position: absolute;
    left: 60px;
    width: 452px;
    top: 652px;
    margin: 0;
    text-align: center;
    font-family: "Oswald", sans-serif;
    font-weight: 500;
    font-size: 30px;
    color: var(--text-white);
    letter-spacing: 0.3px;
  }
  .contact-list {
    position: absolute;
    left: 553px;
    top: 372px;
    margin: 0;
    padding: 0;
    list-style: none;
    font-family: "Roboto", sans-serif;
    font-weight: 300;
    font-size: 35px;
    color: var(--text-white);
  }
  .contact-item {
    display: flex;
    align-items: center;
    gap: 14px;
    height: 50px;
  }
  .contact-item + .contact-item { margin-top: 14px; }
  .contact-item.address { margin-top: 76px; }
  .contact-icon {
    width: 36px;
    height: 40px;
    flex: none;
  }
</style>
</head>
<body>
<main class="card">
  <svg class="card-shape" viewBox="0 0 1200 778" width="1200" height="778" aria-hidden="true">
    <defs>
      <linearGradient id="bandGradient" x1="0" y1="0" x2="0" y2="1">
        <stop offset="0" stop-color="#5aa815"/>
        <stop offset="1" stop-color="#7cc536"/>
      </linearGradient>
    </defs>
    <rect width="1200" height="778" fill="url(#bandGradient)"/>
    <path d="M1200 168 L330 172 Q70 180 0 380" fill="none" stroke="var(--green-light)" stroke-width="10"/>
    <path d="M1200 180 L330 184 Q80 192 0 392 L0 778 L1200 778 Z" fill="var(--card-dark)"/>
  </svg>

  <h1 class="company-title">MAVENBROOK HOLDINGS</h1>

  <div class="brand-mark">
    <span class="brand-dot"></span>
    <p class="brand-name">Mavenbrook Holdings</p>
  </div>

  <p class="tagline">Turning Old Doors Into New Starts</p>

  <ul class="contact-list">
    <li class="contact-item phone">
      <svg class="contact-icon" viewBox="0 0 36 40" aria-hidden="true">
        <path d="M9 6 L14 6 L16 14 L12 17 Q15 25 21 29 L24 25 L31 28 L31 33 Q28 37 23 35 Q10 28 7 14 Q6 8 9 6 Z" fill="var(--green-main)"/>
      </svg>
      <span>678-555-0192</span>
    </li>
    <li class="contact-item web">
      <svg class="contact-icon" viewBox="0 0 36 40" aria-hidden="true">
        <circle cx="18" cy="20" r="14" fill="none" stroke="var(--green-main)" stroke-width="3"/>
        <ellipse cx="18" cy="20" rx="6" ry="14" fill="none" stroke="var(--green-main)" stroke-width="2"/>
        <line x1="4" y1="20" x2="32" y2="20" stroke="var(--green-main)" stroke-width="2"/>
      </svg>
      <span>mavenbrookholdingsllc.example</span>
    </li>
    <li class="contact-item address">
      <svg class="contact-icon" viewBox="0 0 36 40" aria-hidden="true">
        <path d="M18 39 Q6 22 6 15 A12 12 0 0 1 30 15 Q30 22 18 39 Z" fill="var(--green-main)"/>
        <circle cx="18" cy="15" r="5" fill="var(--card-dark)"/>
      </svg>
      <span>2738 Fenwick Lane Duluth GA 30418</span>
    </li>
  </ul>
</main>
</body>
</html>
```